WP website design (Stoneridge)

We need a wordpress design that will incorporate a professional color scheme with company logo in a clean layout. The design needs to consider that this will be developed on a responsive theme. Colors are either 1) green of the logo, and tan and an accent color maybe black; or other highlight for the logo that without the green. Client wants a 'modern' look.

Industry/Entity Type

It Company

Number of Pages Required

1 page

Font styles to use
Serif
Sans Serif

Requirements
Must have
• Navigation - 1) Home 2) Real Estate 3) Auction Calendar 4) About Us 5) Terms & Conditions 6) FAQ 7) Contact Us
• Site will have full width slideshow 960px. Use stock real estate photo. Header will have logo (attached) and contact info:
• Main Office:
• 417 E Hazel Rd
• Marston, VA 24873
• (800) 555-0173
• (540) 555-0148
• Dunmore Office:
• 318 1/2 S. Mill Rd.
• Dunmore, WV 24987
• (304) 645-5645
• Widgets - in the sidebar or footer of site - email signup form; featured auctions; testimonials; Facebook and RSS social icons; link to broker participation form; News and Events Blog.
Nice to have
• use of dropdown menus styling displayed - 1) Current Auctions & 2) Past Auctions under the Auction Calendar link

```html
<!DOCTYPE html>
<html lang="en">
<head>
<meta charset="utf-8">
<title>Stoneridge's Real Estate &amp; Auction</title>
<link rel="stylesheet" href="https://fonts.googleapis.com/css2?family=Raleway:wght@500;600&family=Arimo:wght@400&family=Cinzel:wght@600&display=swap">
<style>
  :root {
    --gold: #f3b54a;
    --gold-deep: #eea12a;
    --ink: #1e1b1a;
    --text: #222;
    --line: #dcdcdc;
    --muted: #9a9a9a;
    --white: #fff;
    --footer: #231f20;
  }
  * { box-sizing: border-box; margin: 0; padding: 0; }
  html, body { width: 862px; height: 1200px; overflow: hidden; background: var(--white); }
  body { position: relative; font-family: "Arimo", Arial, sans-serif; color: var(--text); }
  .abs { position: absolute; }

  /* header */
  .social { left: 634px; top: 5px; display: flex; gap: 6px; }
  .social span { width: 26px; height: 26px; border-radius: 50%; display: block; }
  .social .s1 { background: #3b5a98; } .social .s2 { background: #33a9df; }
  .social .s3 { background: #1a7bb5; } .social .s4 { background: #d0302c; }
  .social .s5 { background: #ee9b2e; }
  .brand { left: 74px; top: 40px; display: flex; align-items: center; gap: 8px;
    font-family: "Raleway", sans-serif; font-weight: 600; font-size: 26px; color: var(--ink); }
  .brand i { width: 14px; height: 14px; border-radius: 50%; background: var(--gold); display: block; }
  .call { left: 638px; top: 52px; }
  .call h4 { font-family: "Cinzel", serif; font-weight: 600; font-size: 13px; color: var(--gold); letter-spacing: .5px; }
  .call p { font-size: 10.5px; color: var(--text); margin-top: 2px; }
  .nav { left: 0; top: 86px; width: 862px; height: 38px; background: var(--gold); }
  .nav a { position: absolute; top: 14px; font-size: 10.5px; color: var(--ink); text-decoration: none; }

  .hero { left: 0; top: 124px; width: 862px; height: 334px;
    background: linear-gradient(180deg, #3f5f86 0%, #8a8d99 35%, #d4a04e 62%, #8b6a2d 78%, #3f4a22 100%); }

  /* welcome */
  .welcome { left: 72px; top: 481px; width: 482px; height: 156px; border: 1px solid var(--line); padding: 0 12px; }
  .welcome h1 { font-family: "Raleway", sans-serif; font-weight: 500; font-size: 18px; color: var(--ink); margin-top: 8px; }
  .welcome h1 em { font-style: normal; color: var(--gold-deep); }
  .rule { width: 301px; height: 2px; background: var(--muted); margin-top: 3px; position: relative; }
  .rule::before { content: ""; position: absolute; left: 0; top: 0; width: 96px; height: 2px; background: var(--gold); opacity: .0; }
  .welcome p { font-size: 10.2px; line-height: 13px; margin-top: 11px; }
  .welcome p + p { margin-top: 13px; }

  .video { left: 582px; top: 481px; width: 201px; height: 145px; background: linear-gradient(135deg, #2a2a2a, #5a4d44 55%, #1a1a1a); }
  .video .bar { position: absolute; left: 0; bottom: 0; width: 100%; height: 15px; background: #111; border-top: 2px solid #c4201d; }
  .video svg.play { position: absolute; left: 91px; top: 58px; }

  /* panels */
  .panel { border: 1px solid var(--line); background: var(--white); }
  .panel-head { height: 28px; background: var(--gold); color: var(--white);
    font-family: "Raleway", sans-serif; font-weight: 600; font-size: 12.5px; padding: 7px 10px 0; text-shadow: 0 1px 1px rgba(0,0,0,.3); }
  .feature { position: relative; height: 82px; }
  .feature .thumb { position: absolute; left: 7px; width: 90px; height: 66px; border: 3px solid #8d8d8d; }
  .thumb.agents { background: linear-gradient(135deg, #c9a26a, #2d7fd0); }
  .thumb.globe { background: linear-gradient(180deg, #4a8fd4, #cfe6f5 55%, #7fb23c); }
  .feature h3 { position: absolute; left: 129px; top: 9px; font-weight: 400; font-size: 10.3px; color: var(--gold-deep); }
  .feature p { position: absolute; left: 129px; top: 21px; width: 290px; font-size: 9.5px; line-height: 13px; }

  .news-item { position: relative; height: 55px; }
  .news-item .thumb { position: absolute; left: 7px; top: 0; width: 68px; height: 47px; background: linear-gradient(180deg, #7fb3e3, #d9c7a3 55%, #5f8a2f); }
  .news-item h5 { position: absolute; left: 84px; top: 4px; font-weight: 400; font-size: 9px; color: var(--gold-deep); }
  .news-item p { position: absolute; left: 85px; top: 17px; width: 95px; font-size: 9.2px; line-height: 13px; }

  .testimonial { left: 582px; top: 885px; width: 204px; height: 175px; background: var(--gold); border-radius: 16px; color: var(--white); padding: 12px 18px; }
  .testimonial h2 { font-family: "Raleway", sans-serif; font-weight: 600; font-size: 13px; letter-spacing: .3px; }
  .testimonial p { font-size: 9.2px; line-height: 16px; margin-top: 6px; text-align: justify; }
  .tail { left: 720px; top: 1058px; }

  /* footer */
  .footer { left: 0; top: 1130px; width: 862px; height: 48px; background: var(--footer); }
  .foot-brand { left: 80px; top: 1103px; display: flex; align-items: center; gap: 7px;
    font-family: "Raleway", sans-serif; font-weight: 600; font-size: 20px; color: var(--ink); }
  .foot-brand i { width: 12px; height: 12px; border-radius: 50%; background: var(--gold); display: block; }
  .badges { left: 518px; top: 1141px; display: flex; gap: 14px; align-items: center; }
  .badges span { display: block; background: #e8e8e8; }
  .copy { left: 0; top: 1178px; width: 862px; height: 22px; background: var(--gold); font-size: 9px; text-align: center; padding-top: 6px; color: var(--ink); }
</style>
</head>
<body>
  <header>
    <div class="social abs" aria-label="Social links"><span class="s1"></span><span class="s2"></span><span class="s3"></span><span class="s4"></span><span class="s5"></span></div>
    <div class="brand abs"><i></i>Stoneridge</div>
    <div class="call abs"><h4>CALL US FREE</h4><p>on 0800 555 0192 &nbsp;8am to 8pm</p></div>
    <nav class="nav abs">
      <a style="left:245px">HOME</a><a style="left:312px">AUCTIONS</a><a style="left:401px">ABOUT US</a>
      <a style="left:489px">BUYERS</a><a style="left:568px">SELLERS</a><a style="left:650px">MEDIA</a><a style="left:719px">CONTACT US</a>
    </nav>
  </header>

  <div class="hero abs" role="img" aria-label="Large Mediterranean-style estate home lit at dusk with palm trees and a fountain"></div>

  <section class="welcome abs">
    <h1><em>WELCOME</em> TO STONERIDGE'S</h1>
    <div class="rule"></div>
    <p>Lorem Ipsum is that it has a more-or-less normal distribution of letters, as opposed to using 'Con-tent here, content here', making it look like readable English. Many desktop publishing packages and web page editors now use Lorem Ipsum as their default model text, and a search for 'lorem ipsum' will uncover many web sites still in their infancy.</p>
    <p>Various versions have evolved over the years, sometimes by accident, sometimes on purpose (injected humour and the like</p>
  </section>

  <div class="video abs" role="img" aria-label="Video player showing a family watching television">
    <svg class="play" width="18" height="20" viewBox="0 0 18 20"><polygon points="2,1 17,10 2,19" fill="#fff"/></svg>
    <div class="bar"></div>
  </div>

  <section class="panel abs" style="left:73px;top:656px;width:481px;height:199px">
    <div class="panel-head">FAMILY OWNED AND OPERATED WITH A FAMILY GUARANTEE</div>
    <div class="feature" style="margin-top:11px"><div class="thumb agents" role="img" aria-label="Hand holding a model house"></div><h3>FURNITURE ' ANTIQUES ' COLLECTIBLES</h3><p>Lorem Ipsum is that it has a more-or-less normal distribution of letters, as opposed to using 'Content here, content here', making it look like readable English. Many desktop publishing packages</p></div>
    <div class="feature"><div class="thumb globe" role="img" aria-label="Hand holding a glass sphere over a green field"></div><h3>FURNITURE ' ANTIQUES ' COLLECTIBLES</h3><p>Lorem Ipsum is that it has a more-or-less normal distribution of letters, as opposed to using 'Content here, content here', making it look like readable English. Many desktop publishing packages</p></div>
  </section>

  <section class="panel abs" style="left:73px;top:883px;width:481px;height:199px">
    <div class="panel-head">FAMILY OWNED AND OPERATED WITH A FAMILY GUARANTEE</div>
    <div class="feature" style="margin-top:11px"><div class="thumb agents" role="img" aria-label="Hand holding a model house"></div><h3>FURNITURE ' ANTIQUES ' COLLECTIBLES</h3><p>Lorem Ipsum is that it has a more-or-less normal distribution of letters, as opposed to using 'Content here, content here', making it look like readable English. Many desktop publishing packages</p></div>
    <div class="feature"><div class="thumb globe" role="img" aria-label="Hand holding a glass sphere over a green field"></div><h3>FURNITURE ' ANTIQUES ' COLLECTIBLES</h3><p>Lorem Ipsum is that it has a more-or-less normal distribution of letters, as opposed to using 'Content here, content here', making it look like readable English. Many desktop publishing packages</p></div>
  </section>

  <aside class="panel abs" style="left:582px;top:656px;width:205px;height:199px">
    <div class="panel-head" style="height:26px">NEWS &amp; EVENTS</div>
    <div style="margin-top:9px">
      <div class="news-item"><div class="thumb" role="img" aria-label="Two-storey suburban house"></div><h5>SETURDAY MARCH 6, 2014</h5><p>Lorem Ipsum is that it has a more-or-less</p></div>
      <div class="news-item"><div class="thumb" role="img" aria-label="Two-storey suburban house"></div><h5>SETURDAY MARCH 6, 2014</h5><p>Lorem Ipsum is that it has a more-or-less</p></div>
      <div class="news-item"><div class="thumb" role="img" aria-label="Two-storey suburban house"></div><h5>SETURDAY MARCH 6, 2014</h5><p>Lorem Ipsum is that it has a more-or-less</p></div>
    </div>
  </aside>

  <aside class="testimonial abs">
    <h2>TESTIMONIALS BLOG</h2>
    <p>&ldquo; simply dummy text of the printing and typesetting industry. Lorem Ipsum has been the industry's standard dummy text ever since the 1500s, when an unknown dummy text ever since printer took a galley of type and scrambled it to make a type. &rdquo;</p>
  </aside>
  <svg class="tail abs" width="30" height="24" viewBox="0 0 30 24"><polygon points="0,0 26,0 28,22" fill="#f3b54a"/></svg>

  <footer>
    <div class="footer abs"></div>
    <div class="foot-brand abs"><i></i>Stoneridge</div>
    <div class="badges abs" aria-label="Partner memberships">
      <span style="width:28px;height:26px;border-radius:50%"></span>
      <span style="width:20px;height:24px"></span>
      <span style="width:22px;height:20px"></span>
      <span style="width:26px;height:26px"></span>
      <span style="width:50px;height:22px"></span>
      <span style="width:40px;height:16px"></span>
    </div>
    <div class="copy abs">Copyright &copy; Stoneridge Real Estate Auction. 2013. &nbsp;All Rights Reserved</div>
  </footer>
</body>
</html>
```